Flyer for Gathering L.I.T. - Evening of Glory!

We are producing a monthly Evening of Glory that supports local Christian Contemporary artists and raises money for charities. We are looking for a flyer design for our flyers, posters, and postcards (some mailed and some handed out). We want to create a modern and impressive flyer that will capture audiences.

Event details -
Tag: experience the night. praise the night.
A Evening of Glory you will not want to miss
Let's worship! Live band covering your favorite popular contemporary Christian music! All ages welcome!
Date: Wednesday, May 27th, 2015
7:00 pm to 8:15 pm
Location: The Harborlight Church
2750 S Maple Ridge Rd; Fort Lauderdale, FL 33871

Event is FREE!! Please bring a donation of gently used clothing items or new toiletry item.
Benefit for: The Hopeful Hands Mission

This month's debut artist: Celeste Varnham - local Christian Singer/Songwriter.

for more details, visit: www.gatheringgloryLIT.example
brought to you by: Margot Tellwell Music
___
Please see our website for style of what we are looking for. Also attached is a template design that I like and would love to see if we can do something like this.

Target Market(s)

all ages - young, older, modern, contemporary - youth

Industry/Entity Type

Artists

Colors
ec1f27
6b449b
ffffff

Requirements
Must have
• Cool design, bring a new "vibe" to Christian music -
• Black design
• worship photos like in the attached template ideas.

```html
<!DOCTYPE html>
<html lang="en">
<head>
<meta charset="utf-8">
<title>Gathering L.I.T. - Evening of Glory</title>
<link href="https://fonts.googleapis.com/css2?family=Oswald:wght@500;700&family=Saira+Condensed:wght@500;800&display=swap" rel="stylesheet">
<style>
:root{
  --stage:#2b2b2e;
  --ink:#0c0b10;
  --red:#ec1f27;
  --purple:#6b449b;
  --violet:#9a2fd0;
  --white:#ffffff;
  --yellow:#ffe21a;
  --glow:#cfe3ff;
}
*{margin:0;padding:0;box-sizing:border-box}
html,body{width:888px;height:1200px;overflow:hidden;background:var(--stage)}
.flyer{position:absolute;left:70px;top:113px;width:752px;height:974px;overflow:hidden;
  background:linear-gradient(180deg,#101014 0%,#1b1822 40%,#2a1840 62%,#6a1fa0 85%,#8e2bc6 100%);
  font-family:"Oswald",sans-serif;color:var(--white)}
.hero-photo{position:absolute;left:0;top:0;width:752px;height:575px;
  background:radial-gradient(ellipse at 50% 40%,rgba(90,90,110,.45),transparent 70%),
  linear-gradient(180deg,#222228 0%,#17161c 55%,#3a2160 100%)}
.brand{position:absolute;top:46px;left:0;width:752px;text-align:center;
  font-family:"Saira Condensed",sans-serif;font-weight:800;font-size:66px;letter-spacing:1px;
  line-height:1;color:var(--white);text-transform:uppercase}
.brand-mark{display:inline-block;width:14px;height:14px;background:var(--red);margin-left:10px;vertical-align:middle}
.streak{position:absolute;left:0;width:752px;height:3px;
  background:linear-gradient(90deg,transparent,rgba(207,227,255,.9) 30%,#fff 50%,rgba(207,227,255,.9) 70%,transparent)}
.streak::before{content:"";position:absolute;left:0;right:0;top:-6px;height:15px;
  background:linear-gradient(90deg,transparent,rgba(160,200,255,.25),transparent)}
.tagline{position:absolute;top:170px;left:0;width:752px;text-align:center;
  font-family:"Saira Condensed",sans-serif;font-weight:800;font-size:60px;line-height:55px;
  color:var(--red);text-transform:uppercase;letter-spacing:2px}
.details{position:absolute;top:332px;left:0;width:752px;text-align:center;
  font-family:"Saira Condensed",sans-serif;font-weight:500;font-size:28px;line-height:39px;text-transform:uppercase}
.details .address{font-size:27px}
.ages{position:absolute;left:222px;top:499px;width:306px;height:52px;border-radius:14px;
  background:linear-gradient(180deg,#ff3a3a,#c4121a);border:2px solid #ff8080;
  color:var(--yellow);font-weight:700;font-size:36px;line-height:46px;text-align:center}
.photo{position:absolute;top:578px;height:166px}
.photo-band{left:0;width:378px;background:linear-gradient(135deg,#3b2f6e,#5a3fa8 55%,#2a2048)}
.photo-stage{left:385px;width:367px;background:linear-gradient(160deg,#3443c8,#2a2f9a 50%,#171c55)}
.lower{position:absolute;left:0;top:745px;width:752px;height:229px;
  background:linear-gradient(180deg,#3a1a66,#7a25b4 55%,#9b34d0)}
.artist-photo{position:absolute;left:305px;top:688px;width:148px;height:286px;border-radius:70px 70px 0 0;
  background:linear-gradient(180deg,#4b6a9a,#2aa7b8 45%,#1c6e86)}
.credits{position:absolute;left:9px;top:780px;width:260px;font-size:19px;line-height:29px;font-weight:500}
.credits .hl{color:var(--yellow)}
.free{position:absolute;left:462px;top:752px;width:284px;height:100px;border:3px solid #e8e8f0;border-radius:24px;
  background:rgba(40,10,70,.45);text-align:center}
.free h2{font-weight:700;font-size:46px;line-height:54px;color:var(--red);margin-top:4px}
.free p{font-family:"Saira Condensed",sans-serif;font-size:14px;line-height:15px;font-weight:500;padding:0 12px}
.links{position:absolute;right:10px;top:870px;text-align:right;font-size:18px;line-height:33px;font-weight:500}
.links .hl{color:var(--yellow)}
</style>
</head>
<body>
<main class="flyer">
  <div class="hero-photo" role="img" aria-label="Worship band performing on a dimly lit stage"></div>

  <div class="brand">Gathering L.I.T.<span class="brand-mark"></span></div>

  <div class="streak" style="top:158px"></div>
  <h1 class="tagline">Experience the night.<br>Praise the night.</h1>
  <div class="streak" style="top:316px"></div>

  <div class="details">
    <p>Date: Wednesday, May 27th, 2015</p>
    <p>7:00 PM to 8:15 PM</p>
    <p>Location: The Harborlight Church</p>
    <p class="address">2750 S Maple Ridge Rd; Fort Lauderdale, FL 33871</p>
  </div>

  <div class="ages">All ages welcome!</div>

  <div class="streak" style="top:574px"></div>
  <div class="photo photo-band" role="img" aria-label="Singer and bass guitarist performing under purple stage light"></div>
  <div class="photo photo-stage" role="img" aria-label="Worship team with raised hands on a blue-lit stage"></div>
  <div class="streak" style="top:743px"></div>

  <div class="lower"></div>
  <div class="artist-photo" role="img" aria-label="Debut artist singing in a patterned turquoise top"></div>

  <div class="credits">
    <p>Benefit for: <span class="hl">The Hopeful Hands Mission</span></p>
    <p class="hl">This month's debut artist: <span>Celeste</span></p>
    <p>Varnham - <span class="hl">local Christian</span></p>
    <p class="hl">Singer/Songwriter.</p>
  </div>

  <div class="free">
    <h2>Event is FREE!!</h2>
    <p>Please bring a donation of gently used clothing items or new toiletry item.</p>
  </div>

  <div class="links">
    <p>visit: <span class="hl">www.gatheringgloryLIT.example</span></p>
    <p>brought to you by: <span class="hl">Margot Tellwell Music</span></p>
  </div>
</main>
</body>
</html>
```